Retirement maintenance and reinstatment brochure

We are looking for a capability statement/brochure outlining our skills and capabilities for maintenance, reinstatement and refurbishment work specific to the requirements of retirement villages in Australia

We are a new company, however our people have significant experience working in this industry

Target Market(s)

Retirement living facilities, aged care facilities, hospitals

Industry/Entity Type

Building

Colors

Designer to choose colors to be used in the design.

Requirements
Must have
• Not alot of wording. Stock images of building refurbishment to retirement living and aged care (carpenters, painters etc)
Nice to have
• 1-2 pages only
Should not have
• alot of meaningless writing

```html
<!DOCTYPE html>
<html lang="en">
<head>
<meta charset="utf-8">
<title>Swift Reach Property Care – Capability Brochure</title>
<link rel="stylesheet" href="https://fonts.googleapis.com/css2?family=Lato:wght@400;700&display=swap">
<style>
  :root {
    --backdrop: #d1d2d4;
    --paper: #ffffff;
    --navy: #163a6b;
    --red: #d1232a;
    --ink: #1d3f74;
    --rule: #2a2a2a;
    --photo-warm-1: #f3d9c4;
    --photo-warm-2: #c9a58a;
    --photo-grass: #7f9a4c;
  }
  * { margin: 0; padding: 0; box-sizing: border-box; }
  html, body { width: 1200px; height: 1200px; overflow: hidden; }
  body {
    background: var(--backdrop);
    font-family: "Lato", Arial, sans-serif;
    color: var(--ink);
    position: relative;
  }
  .page {
    position: absolute;
    width: 772px;
    height: 546px;
    background: var(--paper);
    overflow: hidden;
  }
  .page--cover { left: 213px; top: 41px; }
  .page--inside { left: 216px; top: 613px; }

  /* Cover */
  .cover-photo {
    position: absolute; inset: 0;
    background:
      linear-gradient(180deg, rgba(250,232,220,0.85) 0%, rgba(250,232,220,0) 30%),
      linear-gradient(180deg, var(--photo-warm-1) 0%, #8a8580 35%, var(--photo-warm-2) 60%, #b59a84 82%, var(--photo-grass) 100%);
  }
  .cover-brand {
    position: absolute; left: 35px; top: 465px; width: 197px; height: 81px;
    background: rgba(235, 228, 222, 0.85);
    text-align: center;
  }
  .cover-brand .brand { margin-top: 16px; justify-content: center; }
  .cover-brand .brand-name { font-size: 15px; }
  .cover-phone { font-size: 10.5px; margin-top: 10px; color: var(--ink); }

  .brand { display: flex; align-items: center; gap: 8px; }
  .brand-mark { flex: none; }
  .brand-name { font-weight: 700; color: var(--navy); letter-spacing: 0.2px; white-space: nowrap; }

  /* Inside */
  .blueprint-bg {
    position: absolute; inset: 0;
    background: linear-gradient(135deg, #ffffff 0%, #f2f3f5 45%, #eceef1 100%);
  }
  .inside-brand { position: absolute; left: 12px; top: 46px; }
  .inside-brand .brand-name { font-size: 24px; }

  .intro {
    position: absolute; left: 87px; top: 138px; width: 163px;
    font-size: 9.2px; line-height: 1.42; text-align: justify;
  }
  .intro p + p { margin-top: 11px; }
  .intro .lead { font-size: 10.4px; text-align: left; line-height: 1.3; margin-top: 14px; }
  .column-rule {
    position: absolute; left: 259px; top: 140px; width: 1px; height: 271px; background: var(--rule);
  }
  .notice-icon { position: absolute; left: 126px; top: 403px; }
  .assurance {
    position: absolute; left: 87px; top: 461px; width: 165px;
    font-size: 10.4px; line-height: 1.3;
  }

  .trades-panel {
    position: absolute; left: 293px; top: 101px; width: 444px; height: 374px;
    border: 3px solid var(--navy); background: #fff;
  }
  .trade-photo { position: absolute; }
  .trade-photo--scaffold { left: 3px; top: 3px; width: 110px; height: 178px; background: linear-gradient(180deg, #c9c6c0, #8f9aa6 50%, #6e7a82); }
  .trade-photo--plumbing { left: 3px; top: 183px; width: 110px; height: 86px; background: linear-gradient(135deg, #b9b6b0, #e4e4e2 60%, #8d8c88); }
  .trade-photo--brush { left: 115px; top: 3px; width: 323px; height: 266px; background: linear-gradient(120deg, #ffffff 0%, #f1eef3 45%, #e2d3dc 75%, #c9b3bf 100%); }
  .trade-photo--carpentry { left: 3px; top: 272px; width: 207px; height: 91px; background: linear-gradient(120deg, #6d5a4a, #c7b08e 55%, #e6dccb); }
  .trade-photo--electrical { left: 212px; top: 272px; width: 226px; height: 91px; background: linear-gradient(120deg, #f4f4f4, #e8e6e4 55%, #3d4450); }

  .trades-list {
    position: absolute; right: 10px; top: 4px; text-align: right;
    font-size: 10.6px; line-height: 1.3; color: var(--navy);
  }
  .trades-list h2 { font-size: 10.6px; font-weight: 400; margin-bottom: 14px; }
  .trades-list ul { list-style: none; }
  .trades-list li::before { content: "• "; }

  .contact-line {
    position: absolute; left: 293px; width: 444px; top: 512px;
    text-align: center; font-size: 10.4px;
  }
</style>
</head>
<body>

<section class="page page--cover">
  <div class="cover-photo" role="img" aria-label="Photograph of a cheerful tradesman in overalls and hard hat leaping in front of a house under renovation, warm sunlight"></div>
  <div class="cover-brand">
    <div class="brand">
      <svg class="brand-mark" width="14" height="14" viewBox="0 0 14 14"><circle cx="7" cy="7" r="6" fill="var(--navy)"/></svg>
      <span class="brand-name">SWIFT REACH</span>
    </div>
    <p class="cover-phone">phone number</p>
  </div>
</section>

<section class="page page--inside">
  <div class="blueprint-bg" role="img" aria-label="Faint architectural floor plan drawing in the background"></div>

  <div class="brand inside-brand">
    <svg class="brand-mark" width="36" height="36" viewBox="0 0 36 36"><circle cx="18" cy="18" r="16" fill="var(--navy)"/></svg>
    <span class="brand-name">SWIFT REACH PROPERTY CARE</span>
  </div>

  <div class="intro">
    <p>Swift Reach Property Care is a commercial building and maintenance company established and located on the Sunshine Coast in QLD.</p>
    <p>We have expertise in retirement living and aged care maintenance works such as cleaning and painting programs, reinstatement works including painting and carpet replacement as well as major refurbishment or upgrade works including kitchen and bathroom works, electrical and air conditioning upgrade works.</p>
    <p class="lead">We have the ability to react quickly and complete works with as little as 24 hours notice.</p>
  </div>
  <div class="column-rule"></div>

  <svg class="notice-icon" width="60" height="56" viewBox="0 0 60 56" aria-label="24 hour response">
    <path d="M48 14 A25 25 0 1 0 52 38" fill="none" stroke="var(--navy)" stroke-width="2"/>
    <path d="M44 20 L52 9 L56 21 Z" fill="var(--navy)"/>
    <text x="27" y="36" text-anchor="middle" font-family="Lato, sans-serif" font-weight="700" font-size="20" fill="var(--red)">24</text>
  </svg>

  <p class="assurance">We are licensed and insured, and have a full workplace health and safety compliance system.</p>

  <div class="trades-panel">
    <div class="trade-photo trade-photo--scaffold" role="img" aria-label="Photograph of a painter on scaffolding against a building facade"></div>
    <div class="trade-photo trade-photo--plumbing" role="img" aria-label="Photograph of a plumber fitting a kitchen sink tap"></div>
    <div class="trade-photo trade-photo--brush" role="img" aria-label="Photograph of a worn paintbrush painting a white wall"></div>
    <div class="trade-photo trade-photo--carpentry" role="img" aria-label="Photograph of a carpenter marking timber with a pencil and square"></div>
    <div class="trade-photo trade-photo--electrical" role="img" aria-label="Photograph of an electrician fitting a wall power outlet"></div>

    <div class="trades-list">
      <h2>TRADES WE SPECIALISE IN:</h2>
      <ul>
        <li>Painting and building cleaning</li>
        <li>Carpentry and minor repairs</li>
        <li>Air conditioning upgrades</li>
        <li>Plastering and rendering</li>
        <li>Carpet and floor laying</li>
        <li>Electrical</li>
        <li>Plumbing</li>
      </ul>
    </div>
  </div>

  <p class="contact-line">Contact information - address, phone number, www, e-mail...</p>
</section>

</body>
</html>
```